Bright Harbour Fitness

BRIGHT HARBOUR FITNESS PTY LTD, We are a revolutionary, fresh, new entity to the fitness industry looking to make a mark within and support local communities where we are situated. My business partner and i come with a broad range of skill sets and possess the ability and motivation to ensure our philosophy works - and the philosophy is simple - to help people improve their everyday life and well-being. Be it, helping them with their health and fitness, changing their appearance, improving motivation, setting and achieving goals or by helping them become part of a positive team atmosphere.
Our stores visual appearance, like our training concepts, is quite different to the normal run of the mill gym. It's fresh, it's vibrant, it looks great, and we know it will be a real head turner guaranteed to attract attention. This is definitely the future of fitness.
We would like to see on one side our Info and on the other side our LOGO, colour scheme is in the LOGO.
Final design should tell people "We Help People Look And Feel Bright As The Harbour!

Industry/Entity Type

Training

Contact Information for Business Card

Corwin
0412 386 054
cor@brightharbourfitness.com.au
217 Kestrelvale Rd Wrenfield Bay NSW 2199

Requirements
Must have
• Our Logo

```html
<!DOCTYPE html>
<html lang="en">
<head>
<meta charset="utf-8">
<title>Bright Harbour Fitness – Business Card</title>
<link href="https://fonts.googleapis.com/css2?family=Archivo+Black&family=Open+Sans:wght@700&display=swap" rel="stylesheet">
<style>
  :root {
    --page-bg: #e2e2e2;
    --card-bg: #404040;
    --card-bg-light: #4a4a4a;
    --text-white: #ffffff;
    --accent-yellow: #f3e500;
    --logo-square: #2f8fd6;
    --rule-grey: #8a8a8a;
  }
  * { box-sizing: border-box; margin: 0; padding: 0; }
  html, body {
    width: 1200px;
    height: 814px;
    overflow: hidden;
    background: var(--page-bg);
  }
  .canvas {
    position: relative;
    width: 1200px;
    height: 814px;
    display: flex;
    justify-content: center;
    align-items: center;
    gap: 60px;
  }
  .card {
    width: 380px;
    height: 680px;
    background: linear-gradient(160deg, var(--card-bg-light), var(--card-bg) 60%);
    box-shadow: 0 10px 28px rgba(0,0,0,0.35);
    display: flex;
    flex-direction: column;
    align-items: center;
    color: var(--text-white);
  }

  /* Front: brand side */
  .card-front { justify-content: center; padding-bottom: 40px; }
  .brand-mark {
    width: 150px;
    height: 150px;
    background: var(--logo-square);
    margin-bottom: 56px;
  }
  .brand-name {
    font-family: "Archivo Black", sans-serif;
    color: var(--text-white);
    text-align: center;
    line-height: 1.02;
  }
  .brand-name .line-main { display: block; font-size: 44px; }
  .brand-name .line-sub {
    display: block;
    font-size: 30px;
    letter-spacing: 12px;
    margin-top: 18px;
    padding-left: 12px;
  }
  .brand-rule {
    width: 280px;
    height: 2px;
    background: var(--rule-grey);
    margin-top: 10px;
  }

  /* Back: contact side */
  .card-back { padding-top: 60px; }
  .mini-mark {
    width: 90px;
    height: 90px;
    background: var(--logo-square);
  }
  .person-name {
    font-family: "Archivo Black", sans-serif;
    font-size: 46px;
    letter-spacing: 2px;
    margin-top: 72px;
  }
  .name-rule {
    width: 300px;
    height: 2px;
    background: var(--accent-yellow);
    margin-top: 18px;
    margin-bottom: 34px;
  }
  .contact-list {
    font-family: "Open Sans", sans-serif;
    font-weight: 700;
    text-align: center;
    list-style: none;
  }
  .contact-item { margin-bottom: 14px; }
  .contact-label {
    display: block;
    color: var(--accent-yellow);
    font-size: 18px;
    letter-spacing: 1px;
  }
  .contact-value {
    display: block;
    font-size: 17px;
    line-height: 1.3;
    letter-spacing: 0.5px;
  }
  .contact-value.email { font-size: 16px; }
</style>
</head>
<body>
  <main class="canvas">
    <section class="card card-front" aria-label="Business card front">
      <div class="brand-mark" aria-hidden="true"></div>
      <h1 class="brand-name">
        <span class="line-main">BRIGHT</span>
        <span class="line-main">HARBOUR</span>
        <span class="line-sub">FITNESS</span>
      </h1>
      <div class="brand-rule" aria-hidden="true"></div>
    </section>

    <section class="card card-back" aria-label="Business card back">
      <div class="mini-mark" aria-hidden="true"></div>
      <h2 class="person-name">CORWIN</h2>
      <div class="name-rule" aria-hidden="true"></div>
      <ul class="contact-list">
        <li class="contact-item">
          <span class="contact-label">PHONE</span>
          <span class="contact-value">0412 386 054</span>
        </li>
        <li class="contact-item">
          <span class="contact-label">ADDRESS</span>
          <span class="contact-value">217 Kestrelvale Rd</span>
          <span class="contact-value">Wrenfield Bay NSW 2199</span>
        </li>
        <li class="contact-item">
          <span class="contact-label">EMAIL</span>
          <span class="contact-value email">cor@brightharbourfitness.com.au</span>
        </li>
      </ul>
    </section>
  </main>
</body>
</html>
```